Uncoded front page web design for wedding and event planning company

Hi.

I am launching a wedding and event planning company called Silver Fern Gatherings and need a professional and appealing web design.

So, let me explain my company. I am based in Swindon in Wiltshire but the company will plan weddings and events in Oxfordshire, Wiltshire, Berkshire and London.

We will plan weddings, birthdays, conferences, product launches, fashion shows and conventions but the main focus of the website at this stage should be the weddings with all the other occasions being covered under a single 'events' heading.

My contact details for the website should be:
Maureen Pollard
maureen@silverferngatherings.co.uk
01632 960571 / 07700 900384

I'd like the website to feel clean, bright and elegant and be set against a white or off-white background. My logo is purple and I'd therefore like some purple incorporated into the design although feel free to use a more muted purple as my one might be a little bright? I'm also considering whether it would look nice paired with a little of the colour gold - maybe as a font colour in places?? I'll leave you to figure that one out as your design eye will be better than mine but for your reference below is my purple colour and my suggested gold one....

My purple colour is Pantone 2592 C but feel free to use others
My suggested gold I'm looking at is Pantone 14-1041 TCX

I would like to incorporate a Pagepost feed in the front page if possible, if it looks right. I'd also like to include a variety of pictures as well so I've included a few in a Dropbox folder which is linked below. Please don't feel obliged to use them all by any means (there's loads!) but you've got a few there to play with. If you find any other royalty free images you'd rather use please go ahead but on the understanding I can have them afterwards!

My logo can be retrieved via this Dropbox link...
You'll notice there are 2 styles of placement. Please feel free to use either to fit in with your design...
https://www.filebarrow.net/sh/kq7pw2mzt4xn8bc/BBBLqr5hoPnvtc6S41MkwvaHb?dl=0

The wedding images I have are in this Dropbox folder...
https://www.filebarrow.net/sh/r8ym3vk6fa2lp9q/BBB4dzrTy8kW5nh63LxPeqjsc?dl=0

Other than that, it's over to you.... I can't wait to receive your designs :-)

Ooh....finally just to say, as I receive designs in I think I'll notice aspects that I like and don't like and if I feel they'll be useful for other designers, I'll update my brief below. Thanks

BRIEF UPDATE:
Someone asked if I had a tag-line. Could you use "Creating exquisite occasions today for amazing memories tomorrow"

I realise I hadn't explained what I'd like included on my home page so here's some notes to consider....

A welcome to section for me to start narrative about us and our services which has a button that links to our 'about us' page and 'services' page for further information.

A section that nicely illustrates what services we offer whether that be with icons or pictures.

A section with some photos in that would link to our gallery

A section that shows some customer reviews and blog entries that would link to my reviews page and blog to read more.

And finally a contact us section with my details, social media links and site map.

***
I also need to draw attention to where in the UK my services cover. I was therefore thinking perhaps we could use a picture to demonstrate this where it highlights Wiltshire, Oxfordshire, Berkshire and London on a map thereby demonstrating our areas covered. I have found several English county maps when searching on Google but I'm not sure how to highlight the areas I cover (or dull out the areas I don't) so if you have any ideas on this, I'd really like it incorporated. Thanks. (by the way, for those of you not familiar with English counties, the ones I cover are often abbreviated to Wilts, Oxon, Berks, London, so if you find a suitable map with those names on rather than the full names, you'll know what they are!)

I've found an image of the county map which might work well. I was wondering whether we might somehow grey out the counties I don't cover and just keep the ones I do as mentioned above and then crop it into perhaps a shadowed circle? I've attached a screenshot to the brief.
Updates

I've decided on the tag-line "Creating exquisite occasions today for amazing memories tomorrow" so if that could be included somewhere that would be great. I also need to draw attention to where in the UK my services cover. I was therefore thinking perhaps we could use a picture to demonstrate this where it highlights Wiltshire, Oxfordshire, Berkshire and London on a map thereby demonstrating our areas covered. I have found several English county maps when searching on Google but I'm not sure how to highlight the areas I cover (or dull out the areas I don't) so if you have any ideas on this, I'd really like it incorporated. Thanks. Added Wednesday, June 24, 2015

Target Market(s)

Predominately women aged 25-55

Industry/Entity Type

Wedding Planner

Number of Pages Required

1 page

Font styles to use
Sans Serif
Script

Requirements
Nice to have
• I'd like to see how the colour theme of purple and perhaps a little gold (maybe as a font colour) look against a white background. I've mentioned the Pantone colours in the brief above.
• I've attached a screenshot of a webpage with gold writing in and fonts that I like. Perhaps it could give you inspiration?
Should not have
• I really don't like the font SCRIPTINA so please done use that.

```html
<!DOCTYPE html>
<html lang="en">
<head>
<meta charset="utf-8">
<title>Silver Fern Gatherings</title>
<link rel="stylesheet" href="https://fonts.googleapis.com/css2?family=Open+Sans:wght@400;600;700&family=Parisienne&family=Merriweather:wght@400;700&family=Noticia+Text&display=swap">
<style>
:root{
  --purple:#8f1c9f;
  --purple-deep:#6a1478;
  --purple-soft:#b04fc0;
  --gold:#e9a81a;
  --gold-light:#f5c843;
  --ink:#333;
  --grey:#7a7a7a;
  --dark:#2c2c2e;
  --white:#fff;
}
*{margin:0;padding:0;box-sizing:border-box}
html,body{width:1200px;height:3475px;overflow:hidden}
body{position:relative;background:var(--white);font-family:"Open Sans",sans-serif;color:var(--ink)}
.abs{position:absolute}

/* header */
.site-header{left:0;top:0;width:1200px;height:178px}
.brand{left:132px;top:28px;display:flex;align-items:center;gap:14px}
.brand-mark{width:62px;height:62px;border-radius:50%;background:var(--purple)}
.brand-name{font-family:"Parisienne",cursive;color:var(--purple);font-size:34px;line-height:40px;width:170px}
.main-nav{left:382px;top:0;width:818px;height:65px;background:var(--purple);border-bottom-left-radius:60px 65px}
.main-nav ul{list-style:none;display:flex;gap:36px;padding-left:80px;height:100%;align-items:center}
.main-nav a{color:var(--white);text-decoration:none;font-size:17px}
.interact{left:632px;top:84px;display:flex;align-items:center;gap:10px}
.interact span{font-family:"Parisienne",cursive;color:var(--gold);font-size:26px;margin-right:8px}
.interact i{width:28px;height:28px;border:2px solid #555;border-radius:50%;display:block}

/* hero */
.hero{left:0;top:178px;width:1200px;height:517px;background:
 radial-gradient(ellipse at 40% 20%,#f3e4dc 0,#d8b7a8 22%,transparent 45%),
 radial-gradient(ellipse at 80% 40%,#6d5448 0,transparent 50%),
 linear-gradient(135deg,#4b3a30,#8a6b5a 45%,#3a2c25)}
.hero-caption{left:0;top:578px;width:1200px;height:112px;background:rgba(40,40,40,.55);display:flex;align-items:center;justify-content:center;text-align:center;color:var(--white);font-family:"Noticia Text",serif;font-size:36px;line-height:42px}
.hero-arrow{top:610px}

/* welcome */
.section-title{width:1200px;left:0;text-align:center;color:var(--purple);font-family:"Parisienne",cursive;font-weight:400}
.divider{left:450px;width:300px;height:2px;background:linear-gradient(90deg,transparent,#ccc,transparent)}
.welcome-text{left:132px;width:570px;font-size:13.5px;line-height:19.5px;color:#555}
.btn-more{left:132px;top:1073px;width:128px;height:37px;background:var(--purple);color:var(--white);font-size:12px;font-weight:700;display:flex;align-items:center;padding-left:14px;gap:14px;border-radius:3px}
.photo-circle{border-radius:50%;border:5px solid var(--white);box-shadow:0 6px 18px rgba(0,0,0,.3)}

/* services */
.services{left:0;top:1170px;width:1200px;height:422px;background:
 radial-gradient(ellipse at 80% 30%,#6b4a4d,transparent 55%),
 linear-gradient(180deg,#2a2324,#3d3232 50%,#241e1e)}
.service{width:160px;text-align:center;color:var(--white)}
.service .icon{width:120px;height:120px;margin:0 auto;border-radius:50%;border:8px solid #8d8a87;background:radial-gradient(circle at 40% 35%,var(--gold-light),#d28d0a);display:flex;align-items:center;justify-content:center}
.service .label{margin-top:18px;font-family:"Noticia Text",serif;font-size:21px;line-height:22px;text-transform:uppercase}

/* gallery */
.thumb{top:1773px;width:206px;height:139px;border-radius:10px;box-shadow:0 6px 14px rgba(0,0,0,.35)}

/* reviews / blog */
.feature-band{left:0;top:1981px;width:1200px;height:375px;background:linear-gradient(115deg,#5a1a78,#8a3fb0 45%,#6c2b98 70%,#4d1770)}
.band-head{top:2020px;color:var(--white);font-size:22px;text-transform:uppercase}
.band-ctrl{top:2018px;color:var(--white);font-size:22px;font-weight:700;letter-spacing:4px}
.entry{width:320px}
.entry .who{color:var(--white);font-size:15px;font-weight:600;line-height:20px}
.entry .who em{font-style:normal;color:var(--gold-light);font-weight:400}
.entry p{color:#eadff0;font-size:13px;line-height:18px;margin-top:4px}
.avatar{width:80px;height:80px;border-radius:50%;border:3px solid var(--white)}

/* coverage */
.coverage-title{left:132px;top:2398px;font-family:"Noticia Text",serif;font-weight:400;font-size:27px;line-height:38px;color:#222}
.county{left:132px;width:234px;height:44px;background:linear-gradient(90deg,rgba(255,255,255,0),#f1f1f1);color:var(--purple);font-family:"Noticia Text",serif;font-size:25px;text-align:right;padding-right:8px;line-height:44px}
.coverage-note{left:162px;top:2834px;width:874px;height:90px;background:#7b7b7b;border-radius:10px;color:var(--white);font-size:15px;line-height:22px;text-align:center;display:flex;align-items:center;padding:0 20px}

/* contact */
.contact{left:0;top:2970px;width:1200px;height:454px;background:radial-gradient(ellipse at 80% 30%,#5a5a5a,transparent 60%),linear-gradient(180deg,#3b3b3d,#2a2a2c)}
.contact-card{left:135px;top:3064px;width:290px;height:290px;border-radius:50%;background:var(--purple);color:var(--white);text-align:center;padding-top:100px;font-size:14px;line-height:21px}
.contact-card .name{font-family:"Parisienne",cursive;font-size:32px;line-height:36px;margin-bottom:12px}
.gold-head{color:var(--gold);font-family:"Noticia Text",serif;font-size:26px}
.field{color:var(--white);font-size:13px;border-bottom:1px solid #aaa;height:26px}
.submit{left:417px;top:3309px;width:107px;height:32px;background:var(--white);color:#222;font-size:14px;font-weight:700;padding-left:12px;line-height:32px}
.social{left:935px;display:flex;align-items:center;gap:16px;color:var(--white);font-size:12px}
.social i{width:48px;height:48px;border-radius:50%;border:3px solid #555;display:block}

/* footer */
.site-footer{left:0;top:3424px;width:1200px;height:51px;background:var(--purple);color:var(--white);font-size:13px;padding-left:137px;line-height:51px}
</style>
</head>
<body>

<header class="site-header abs">
  <div class="brand abs"><span class="brand-mark"></span><span class="brand-name">Silver Fern Gatherings</span></div>
  <nav class="main-nav abs"><ul>
    <li><a href="#">Home</a></li><li><a href="#">About Us</a></li><li><a href="#">Event Planning</a></li>
    <li><a href="#">Blog</a></li><li><a href="#">Testimonials</a></li><li><a href="#">Contact Us</a></li>
  </ul></nav>
  <div class="interact abs"><span>Interact With Us!</span><i></i><i></i><i></i><i></i><i></i><i></i><i></i><i></i></div>
</header>

<section>
  <div class="hero abs" role="img" aria-label="Photo of a wedding reception table with a flower centrepiece, glasses and a table number card"></div>
  <div class="hero-caption abs">Creating Exquisite Occasions Today For Amazing<br>Memories Tomorrow</div>
  <svg class="hero-arrow abs" style="left:80px" width="28" height="50" viewBox="0 0 28 50"><path d="M24 3 4 25l20 22" fill="none" stroke="#fff" stroke-width="3"/></svg>
  <svg class="hero-arrow abs" style="left:1092px" width="28" height="50" viewBox="0 0 28 50"><path d="M4 3l20 22L4 47" fill="none" stroke="#fff" stroke-width="3"/></svg>
</section>

<section class="welcome">
  <h1 class="section-title abs" style="top:735px;font-size:54px">Welcome To Silver Fern</h1>
  <div class="divider abs" style="top:822px"></div>
  <p class="welcome-text abs" style="top:872px">Lorem ipsum dolor sit amet, consectetuer adipiscing elit, sed diam nonummy nibh euismod tincidunt ut laoreet dolore magna aliquam erat volutpat. Ut wisi enim ad minim veniam, quis nostrud exerci tation ullamcorper suscipit lobortis nisl ut aliquip ex ea commodo consequat. Duis autem vel eum iriure dolor in hendrerit in vulputate velit esse molestie consequat, vel illum dolore eu feugiat nulla facilisis at vero eros et accumsan et iusto odio dignissim qui blandit praesent luptatum zzril delenit augue duis dolore te feugait nulla facilisi.</p>
  <p class="welcome-text abs" style="top:1018px">Lorem ipsum dolor sit amet, consectetuer adipiscing elit, sed diam nonummy nibh euismod tincidunt ut laoreet dolore magna aliquam erat volutpat.</p>
  <div class="btn-more abs">READ MORE <span>»</span></div>
  <div class="photo-circle abs" style="left:725px;top:880px;width:200px;height:200px;background:radial-gradient(circle,#e6eef2,#9fb0ba 60%,#6f7e88)" role="img" aria-label="Photo of a banquet hall set with white tables"></div>
  <div class="photo-circle abs" style="left:872px;top:855px;width:190px;height:190px;background:radial-gradient(circle at 45% 55%,#f0d27a,#d95a7a 45%,#4a9ad8 80%)" role="img" aria-label="Photo of a birthday party with balloons"></div>
</section>

<section>
  <div class="services abs" role="img" aria-label="Dimmed photo of an event table with glassware"></div>
  <h2 class="section-title abs" style="top:1215px;font-size:48px;color:#fff">Services We Offer</h2>
  <div class="divider abs" style="top:1292px;background:linear-gradient(90deg,transparent,#888,transparent)"></div>

  <div class="service abs" style="left:112px;top:1358px"><div class="icon"><svg width="56" height="50" viewBox="0 0 56 50"><circle cx="21" cy="29" r="15" fill="none" stroke="#fff" stroke-width="5"/><circle cx="35" cy="29" r="15" fill="none" stroke="#fff" stroke-width="5"/><path d="M28 2l5 7-5 5-5-5z" fill="#fff"/></svg></div><div class="label">Weddings</div></div>
  <div class="service abs" style="left:272px;top:1358px"><div class="icon"><svg width="50" height="54" viewBox="0 0 50 54"><path d="M20 4 6 50h36z" fill="none" stroke="#fff" stroke-width="5" stroke-linejoin="round"/><circle cx="20" cy="4" r="4" fill="#fff"/></svg></div><div class="label">Birthdays</div></div>
  <div class="service abs" style="left:434px;top:1358px"><div class="icon"><svg width="40" height="56" viewBox="0 0 40 56"><rect x="11" y="2" width="18" height="32" rx="9" fill="#fff"/><path d="M4 24c0 12 7 18 16 18s16-6 16-18M20 42v10M10 53h20" fill="none" stroke="#fff" stroke-width="4"/></svg></div><div class="label">Conferences</div></div>
  <div class="service abs" style="left:599px;top:1358px"><div class="icon"><svg width="56" height="50" viewBox="0 0 56 50"><path d="M4 22 28 4l24 18v24H4z" fill="none" stroke="#fff" stroke-width="5" stroke-linejoin="round"/><rect x="18" y="24" width="20" height="14" fill="#fff"/></svg></div><div class="label">Product<br>Launches</div></div>
  <div class="service abs" style="left:759px;top:1358px"><div class="icon"><svg width="36" height="60" viewBox="0 0 36 60"><path d="M12 2h12v10l-4 12 14 34H2l14-34-4-12z" fill="#fff"/></svg></div><div class="label">Fashion<br>Shows</div></div>
  <div class="service abs" style="left:923px;top:1358px"><div class="icon"><svg width="50" height="56" viewBox="0 0 50 56"><circle cx="25" cy="9" r="7" fill="#fff"/><rect x="4" y="22" width="42" height="8" fill="#fff"/><path d="M14 30h22l-4 24H18z" fill="#fff"/></svg></div><div class="label">Conventions</div></div>
</section>

<section class="gallery">
  <h2 class="section-title abs" style="top:1622px;font-size:48px">Our Gallery</h2>
  <div class="divider abs" style="top:1700px"></div>
  <svg class="abs" style="left:80px;top:1818px" width="24" height="50" viewBox="0 0 24 50"><path d="M22 2 3 25l19 23" fill="none" stroke="#ccc" stroke-width="2"/></svg>
  <svg class="abs" style="left:1092px;top:1818px" width="24" height="50" viewBox="0 0 24 50"><path d="M2 2l19 23L2 48" fill="none" stroke="#ccc" stroke-width="2"/></svg>
  <div class="thumb abs" style="left:137px;background:linear-gradient(135deg,#c8263a,#f08a3a 55%,#7a1a2a)" role="img" aria-label="Photo of a reception venue lit in red"></div>
  <div class="thumb abs" style="left:375px;background:linear-gradient(135deg,#d9c2a0,#b46a5a 50%,#5a7aa8)" role="img" aria-label="Photo of party guests celebrating"></div>
  <div class="thumb abs" style="left:616px;background:linear-gradient(135deg,#3a2418,#c27a3a 50%,#2a1a12)" role="img" aria-label="Photo of a candlelit dinner table"></div>
  <div class="thumb abs" style="left:855px;background:linear-gradient(135deg,#1e3a6a,#c0543a 55%,#25335a)" role="img" aria-label="Photo of a conference speaker on stage"></div>
</section>

<section>
  <div class="feature-band abs"></div>
  <div class="band-head abs" style="left:132px">Customer Reviews</div>
  <div class="band-ctrl abs" style="left:540px">‹ ›</div>
  <div class="abs" style="left:600px;top:2030px;width:1px;height:280px;background:rgba(255,255,255,.25)"></div>
  <div class="band-head abs" style="left:640px">From the Blog</div>
  <div class="band-ctrl abs" style="left:1030px">‹ ›</div>

  <div class="avatar abs" style="left:131px;top:2078px;background:radial-gradient(circle,#c99a86,#6a3a30)" role="img" aria-label="Customer portrait"></div>
  <div class="entry abs" style="left:239px;top:2076px"><div class="who">Elodie, <em>Sr. Executive</em></div><p>Lorem ipsum dolor sit amet, consecteretu ew adipiscing ir elit, sed diam nonummy nibh euismod er tincidunt ut laore..</p></div>
  <div class="avatar abs" style="left:131px;top:2203px;background:radial-gradient(circle,#c99a86,#6a3a30)" role="img" aria-label="Customer portrait"></div>
  <div class="entry abs" style="left:239px;top:2201px"><div class="who">Elodie, <em>Sr. Executive</em></div><p>Lorem ipsum dolor sit amet, consecteretu ew adipiscing ir elit, sed diam nonummy nibh euismod er tincidunt ut laore..</p></div>

  <div class="avatar abs" style="left:646px;top:2078px;background:radial-gradient(circle,#f3d0d8,#b24a6a 60%,#4a7a4a)" role="img" aria-label="Blog post thumbnail"></div>
  <div class="entry abs" style="left:751px;top:2076px"><div class="who">Lorem ipsum dolor sit amet,<br><em>on 23 June, 2015</em></div><p>Lorem ipsum dolor sit amet, consecteretu ew adipiscing ir elit, sed diam nonummy nibh euismod...</p></div>
  <div class="avatar abs" style="left:646px;top:2203px;background:radial-gradient(circle,#f3d0d8,#b24a6a 60%,#4a7a4a)" role="img" aria-label="Blog post thumbnail"></div>
  <div class="entry abs" style="left:751px;top:2201px"><div class="who">Lorem ipsum dolor sit amet,<br><em>on 23 June, 2015</em></div><p>Lorem ipsum dolor sit amet, consecteretu ew adipiscing ir elit, sed diam nonummy nibh euismod...</p></div>
</section>

<section class="coverage">
  <div class="abs" style="left:330px;top:2356px;width:870px;height:614px;background:radial-gradient(ellipse at 48% 52%,#c45ad4 0,#d9a3e2 14%,#ececec 32%,#f6f6f6 60%,#fff 85%)" role="img" aria-label="Map of southern England counties with Oxfordshire, Berkshire, Wiltshire and London highlighted in purple"></div>
  <h2 class="coverage-title abs">Our Services covering mainly<br>these countries of England</h2>
  <div class="county abs" style="top:2487px">Oxfordshire/Oxon</div>
  <div class="county abs" style="top:2545px">Berkshire/Berks</div>
  <div class="county abs" style="top:2601px">Wiltshire/Wilts</div>
  <div class="county abs" style="top:2659px">London</div>
  <svg class="abs" style="left:0;top:0" width="1200" height="3000" viewBox="0 0 1200 3000">
    <g stroke="#666" stroke-width="2.5">
      <line x1="366" y1="2509" x2="751" y2="2618"/>
      <line x1="366" y1="2567" x2="778" y2="2692"/>
      <line x1="366" y1="2623" x2="674" y2="2750"/>
      <line x1="366" y1="2681" x2="927" y2="2683"/>
    </g>
    <g fill="#fff"><circle cx="751" cy="2618" r="7"/><circle cx="778" cy="2692" r="7"/><circle cx="674" cy="2750" r="7"/><circle cx="927" cy="2683" r="7"/></g>
  </svg>
  <p class="coverage-note abs">Lorem ipsum dolor sit amet, consectetuer adipiscing elit, sed diam nonummy nibh euismod tincidunt ut laoreet dolore magna aliquam erat volutpat. Ut wisi enim ad minim veniam, quis nostrud exerci tation ullamcorper suscipit lobortis nisl ut aliquip ex ea commodo consequat. Duis autem vel eum iriure.</p>
</section>

<section>
  <div class="contact abs" role="img" aria-label="Dimmed photo of hands typing on a keyboard"></div>
  <h2 class="section-title abs" style="top:3005px;font-size:46px;color:#fff">Get In Touch</h2>
  <div class="divider abs" style="top:3078px;background:linear-gradient(90deg,transparent,#777,transparent)"></div>

  <div class="contact-card abs">
    <div class="name">Maureen Pollard</div>
    WRITE TO US:<br>maureen@silverferngatherings.co.uk<br><br>YOU CAN ALSO CALL US:<br>01632 960571<br>07700 900384
  </div>

  <div class="gold-head abs" style="left:405px;top:3104px">Send Us your query</div>
  <div class="field abs" style="left:429px;top:3156px;width:200px">First Name</div>
  <div class="field abs" style="left:653px;top:3156px;width:200px">Last Name</div>
  <div class="field abs" style="left:429px;top:3201px;width:200px">Email Address</div>
  <div class="field abs" style="left:663px;top:3201px;width:190px">Phone Number</div>
  <div class="field abs" style="left:429px;top:3243px;width:424px">Email Address</div>
  <div class="submit abs">SUBMIT</div>

  <div class="gold-head abs" style="left:936px;top:3102px">Follow Us</div>
  <div class="social abs" style="top:3148px"><i style="background:#2f5a9a"></i>PAGEPOST</div>
  <div class="social abs" style="top:3204px"><i style="background:#2fa3d8"></i>CHIRPLINE</div>
  <div class="social abs" style="top:3259px"><i style="background:#1f6fa8"></i>WORKLINK</div>
  <div class="social abs" style="top:3315px"><i style="background:#c8432f"></i>RSS FEED</div>
</section>

<footer class="site-footer abs">Copyright 2015 SILVER FERN GATHERINGS. All Rights Reserved.
  <svg class="abs" style="left:780px;top:0" width="420" height="51" viewBox="0 0 420 51"><path d="M0 0h420v51H60C40 51 40 0 0 0z" fill="#2a2a2c"/></svg>
</footer>

</body>
</html>
```